An Engineering book catering oil and gas engineering students and professionals

I need a logo for the cover page of the book. I suggest you watch on vidstreamo the drilling for oil and gas video not more than 10 mins. Once you have watched it then you can go ahead and watch the video on Borehole Equilibrium Control Technique. I am currently the only person in the industry who is teaching the most comprehensive course on this technique hence the book on the same topic which will compliment my teachings to my attendees.
While you are designing the logo keep oil and gas drilling, high pressure , high temperature, pressure gauges, reservoir rock where oil and gas are trapped. if you like I can also put some pictures here and you can have a look.

Borehole Equilibrium Control is all about balancing the pressure with the pressure that is inside the reservoir rock. I will try to attach some pictures later. With the light fluid inside the well we apply pressure from surface that make the pressure inside the well equal to the formation or reservoir rock pressure.

The book design has to portray an engineering book cover so try to avoid too much colour please. My name is Rafiq (Raf) Dorvani therefore the book should have my name on the stem of the book. At the front the design should be elegant with an easy and readable title of the book.

The name of the book is "Borehole Equilibrium Control" (Engineering & Operations). Plz avoid rig or pump jack pictures it is too old. Work with pressure gauge, pressure or balancing the pressure etc. You can also place words like BHCP, ECD, ESD, DIF. IME, WC Matrix, RCD, ACM, RPDS, NSD, CT. Please dont put pictures of drill machines, oil and gas drilling is not done with drill machines :). Moreover, the book size will be smaller than the A4 page meaning Length 24 inches width of 17 inches. See what you come up with and we go from there

```html
<!DOCTYPE html>
<html lang="en">
<head>
<meta charset="utf-8">
<title>Borehole Equilibrium Control Technique — Book Cover</title>
<link href="https://fonts.googleapis.com/css2?family=Saira+Extra+Condensed:wght@500;600&display=swap" rel="stylesheet">
<style>
  :root {
    --stage: #aab1ba;
    --paper: #ffffff;
    --paper-shade: #f1f1f1;
    --ink: #262626;
    --yellow: #fecf45;
    --yellow-deep: #f6c63a;
    --black: #232323;
    --sea-deep: #1f4f7e;
    --sea-mid: #4f86b8;
    --sky: #9cc4e6;
  }
  html, body {
    margin: 0;
    padding: 0;
    width: 1200px;
    height: 1200px;
    overflow: hidden;
    background: var(--stage);
  }
  .cover {
    position: absolute;
    left: 225px;
    top: 32px;
    width: 752px;
    height: 1109px;
    background: linear-gradient(160deg, var(--paper) 40%, var(--paper-shade) 100%);
    overflow: hidden;
  }
  .top-band {
    position: absolute;
    left: 0; top: 0;
    width: 687px; height: 112px;
    background: var(--yellow);
  }
  .top-block {
    position: absolute;
    left: 687px; top: 0;
    width: 65px; height: 112px;
    background: var(--black);
  }
  .cover-text {
    position: absolute;
    left: 0; top: 0;
    width: 752px; height: 1109px;
  }
  .title-line {
    font-family: "Saira Extra Condensed", "Arial Narrow", sans-serif;
    font-weight: 600;
    font-size: 112px;
    fill: var(--ink);
  }
  .author {
    font-family: "Saira Extra Condensed", "Arial Narrow", sans-serif;
    font-weight: 500;
    font-size: 50px;
    fill: var(--ink);
  }
  .cover-photo {
    position: absolute;
    left: 0; top: 461px;
    width: 687px; height: 406px;
    background:
      radial-gradient(ellipse at 78% 45%, rgba(255, 235, 170, 0.55) 0%, rgba(255, 235, 170, 0) 45%),
      linear-gradient(100deg, rgba(214, 178, 60, 0.0) 20%, rgba(214, 178, 60, 0.55) 75%, rgba(214, 178, 60, 0.35) 100%),
      linear-gradient(180deg, var(--sky) 0%, #d7dfe2 38%, var(--sea-mid) 60%, var(--sea-deep) 100%);
  }
  .side-strip {
    position: absolute;
    left: 687px; top: 459px;
    width: 65px; height: 408px;
    background: var(--yellow-deep);
  }
  .bottom-band {
    position: absolute;
    left: 0; top: 1039px;
    width: 752px; height: 70px;
    background: var(--black);
  }
</style>
</head>
<body>
  <main class="cover">
    <div class="top-band"></div>
    <div class="top-block"></div>
    <div class="cover-photo" role="img" aria-label="Offshore oil and gas platform at sea overlaid with a cluster of round oil and gas industry icons"></div>
    <div class="side-strip"></div>
    <svg class="cover-text" viewBox="0 0 752 1109" xmlns="http://www.w3.org/2000/svg">
      <text class="title-line" x="80" y="258" textLength="598" lengthAdjust="spacingAndGlyphs">Borehole Equilibrium</text>
      <text class="title-line" x="80" y="369" textLength="560" lengthAdjust="spacingAndGlyphs">Control Technique</text>
      <text class="author" x="79" y="981" textLength="205" lengthAdjust="spacingAndGlyphs">Rafiq Dorvani</text>
    </svg>
    <div class="bottom-band"></div>
  </main>
</body>
</html>
```